Builder Supply Needs Eye-catching Poster Design for Upcoming Workshop

We're doing a concrete carving workshop. It's a new concept in our area. We need a poster that will get people asking questions about it.

Needs to have:
- Our logo somewhere
- Picture(s) of concrete carving (attached)
- Should say, "We're hosting a vertical carving workshop. Details to be announced. Sign up for more information"

Target Market(s)

Contractors

Industry/Entity Type

Concrete

Font styles to use
Sans Serif

Requirements
Must have
• - Our logo somewhere
• - Picture(s) of concrete carving (attached)
• - Should say, "We're hosting a vertical carving workshop. Details to be announced. Sign up for more information"
• - Needs to be high enough resolution to be printed at 24 x 36 by Quillo Press
Nice to have
• Eye-catching design

```html
<!DOCTYPE html>
<html lang="en">
<head>
<meta charset="utf-8">
<title>Vertical Carving Workshop</title>
<link href="https://fonts.googleapis.com/css2?family=Oswald:wght@500;700&display=swap" rel="stylesheet">
<style>
  :root {
    --ink: #ffffff;
    --accent: #e3312d;
    --stone-light: #9a9d9c;
    --stone-mid: #6f7373;
    --stone-dark: #3e4242;
  }
  html, body {
    margin: 0;
    padding: 0;
    width: 849px;
    height: 1200px;
    overflow: hidden;
    background: var(--stone-dark);
  }
  .poster {
    position: relative;
    width: 849px;
    height: 1200px;
    overflow: hidden;
    font-family: "Oswald", "Arial Narrow", sans-serif;
    color: var(--ink);
  }
  .carving-photo {
    position: absolute;
    inset: 0;
    background:
      radial-gradient(ellipse at 70% 20%, var(--stone-light) 0%, transparent 55%),
      radial-gradient(ellipse at 20% 85%, var(--stone-light) 0%, transparent 50%),
      linear-gradient(160deg, var(--stone-mid) 0%, var(--stone-dark) 45%, var(--stone-mid) 70%, var(--stone-dark) 100%);
  }
  .intro {
    position: absolute;
    left: 79px;
    top: 104px;
    margin: 0;
    font-weight: 500;
    font-size: 25px;
    letter-spacing: 1px;
  }
  .headline {
    position: absolute;
    inset: 0;
  }
  .headline text {
    font-family: "Oswald", "Arial Narrow", sans-serif;
    font-weight: 700;
    font-size: 150px;
    fill: var(--ink);
  }
  .headline line {
    stroke: var(--accent);
    stroke-width: 3;
  }
  .details {
    position: absolute;
    left: 79px;
    top: 995px;
    margin: 0;
    font-weight: 700;
    font-size: 23px;
    line-height: 1.2;
    letter-spacing: 0.5px;
    text-transform: uppercase;
  }
  .brand {
    position: absolute;
    right: 60px;
    top: 1010px;
    text-align: center;
    font-weight: 700;
    line-height: 1;
  }
  .brand-name {
    display: block;
    font-size: 48px;
    letter-spacing: 2px;
  }
  .brand-tag {
    display: block;
    font-size: 16px;
    letter-spacing: 3px;
    margin-top: 6px;
    text-transform: uppercase;
  }
</style>
</head>
<body>
<main class="poster">
  <div class="carving-photo" role="img" aria-label="Black and white photo of carved concrete made to look like weathered logs and stone"></div>

  <p class="intro">WE'RE HOSTING A</p>

  <svg class="headline" width="849" height="1200" viewBox="0 0 849 1200" aria-label="Vertical carving workshop">
    <g transform="rotate(-7.5 85 425)">
      <line x1="-300" y1="445" x2="1200" y2="445"/>
      <line x1="-300" y1="585" x2="1200" y2="585"/>
      <line x1="-300" y1="725" x2="1200" y2="725"/>
      <line x1="-300" y1="865" x2="1200" y2="865"/>
      <line x1="-300" y1="920" x2="1200" y2="920"/>
      <text x="85" y="425" textLength="680" lengthAdjust="spacingAndGlyphs">VERTICA</text>
      <text x="85" y="565" textLength="680" lengthAdjust="spacingAndGlyphs">L CARVI</text>
      <text x="85" y="705" textLength="500" lengthAdjust="spacingAndGlyphs">NG WO</text>
      <text x="85" y="845" textLength="680" lengthAdjust="spacingAndGlyphs">RKSHOP</text>
    </g>
  </svg>

  <p class="details">Details to be<br>announced.<br>Sign up for more<br>information.</p>

  <div class="brand">
    <span class="brand-name">MARLOW</span>
    <span class="brand-tag">Concrete Supply</span>
  </div>
</main>
</body>
</html>
```